Beautiful Quotes For Social Media Posts

We are looking for 5 beautifully designed quotes for our social media account.

Inspiration of styles we like in both style and color along with a few of our favorite fonts (you are NOT limited to these fonts this is just to give you an idea):
https://quillmorestudio.example.com/s/k7p2vx9tqa41mzn8wbd3ce6hr5lf0y2j

*These fonts are property of Quillmore Studio. You do not have permission/rights to use them outside of this assignment*

Quotes to use (5):
“Only those who dare to fail greatly can ever achieve greatly.” –Vernon T. Ashgrove
“Don’t go through life, grow through life.” – Milo Pendrake
“Follow your bliss and the universe will open doors where there were only walls.” – Arthur Venholm
“If you don’t like the road you’re walking, start paving another one.” – Greta Mossley
“Life is like riding a bicycle. To keep your balance, you must keep moving.” —Lucian Thornwick

File Specifics:
- JPG
- 10x10 in size (square)
- Please include @QuillmoreStudio in the bottom right left or center of each design

Brand Details:
Soft but rich pastel and bright colors.
Hand Drawn florals, doodles and art
Handwritten looking fonts
Artsy, Creative, Girl and Inspiring

```html
<!DOCTYPE html>
<html lang="en">
<head>
<meta charset="utf-8">
<title>Quote Social Posts — Quillmore Studio</title>
<link rel="stylesheet" href="https://fonts.googleapis.com/css2?family=Amatic+SC:wght@700&family=Caveat+Brush&family=EB+Garamond&family=Patrick+Hand+SC&family=Roboto:wght@400&display=swap">
<style>
  :root {
    --board-pink: #ffb6bc;
    --board-blush: #fdd6d6;
    --board-sage: #b4c2b6;
    --board-rose: #f3a9b0;
    --ink: #141414;
    --label-grey: #4a4a4a;
    --hot-pink: #ee4f93;
    --teal: #13c3b4;
    --deep-teal: #0e6b6c;
    --soft-pink: #fdd3da;
    --mustard: #f6b731;
    --sun: #ffdf4a;
    --coral: #fd8a60;
    --orange: #fb963c;
    --navy: #2b1d6b;
    --white: #ffffff;
  }
  * { margin: 0; padding: 0; box-sizing: border-box; }
  html, body { width: 900px; height: 1200px; overflow: hidden; }
  body { background: var(--board-pink); position: relative; font-family: "Roboto", sans-serif; }

  .board-shapes { position: absolute; inset: 0; }
  .board-label {
    position: absolute; left: 33px; top: 48px;
    font-size: 16px; line-height: 22px; color: var(--label-grey);
  }

  .post {
    position: absolute; overflow: hidden;
    box-shadow: 4px 6px 10px rgba(90, 40, 50, 0.35);
  }
  .post .art { position: absolute; inset: 0; }
  .handle {
    position: absolute; font-family: "EB Garamond", serif;
    font-size: 11px; color: #333;
  }
  .line { position: absolute; left: 0; right: 0; text-align: center; white-space: nowrap; }

  /* Post 1 — grow through life */
  .post-grow { left: 49px; top: 199px; width: 392px; height: 392px; background: var(--white); }
  .post-grow .quote { font-family: "Amatic SC", sans-serif; color: var(--ink); text-transform: uppercase; }
  .post-grow .line { left: 120px; right: 14px; line-height: 1; }
  .post-grow .accent-pink { color: var(--hot-pink); }
  .post-grow .accent-teal { color: var(--teal); }
  .post-grow .author {
    position: absolute; right: 21px; top: 326px; text-transform: uppercase;
    font-family: "Amatic SC", sans-serif; font-size: 24px; color: var(--ink);
  }
  .post-grow .handle { left: 16px; bottom: 14px; }

  /* Post 2 — balance */
  .post-balance { left: 472px; top: 199px; width: 392px; height: 392px; background: var(--sun); }
  .post-balance .quote { font-family: "Caveat Brush", cursive; color: var(--white); font-size: 32px; }
  .post-balance .line { left: 92px; right: 18px; line-height: 36px; }
  .post-balance .accent-yellow { color: var(--sun); }
  .post-balance .author {
    position: absolute; right: 21px; top: 280px;
    font-family: "Caveat Brush", cursive; font-size: 16px; color: var(--deep-teal);
  }
  .post-balance .handle { right: 14px; bottom: 14px; }

  /* Post 3 — follow your bliss */
  .post-bliss { left: 239px; top: 628px; width: 405px; height: 405px; background: var(--orange); }
  .post-bliss .quote { font-family: "Patrick Hand SC", cursive; font-size: 24px; text-transform: uppercase; }
  .post-bliss .line { left: 70px; right: 70px; line-height: 31px; }
  .post-bliss .ink-navy { color: var(--navy); }
  .post-bliss .ink-white { color: var(--white); }
  .post-bliss .big { font-size: 28px; }
  .post-bliss .author {
    position: absolute; right: 59px; top: 186px; text-transform: uppercase;
    font-family: "Patrick Hand SC", cursive; font-size: 12px; color: var(--navy);
  }
  .post-bliss .handle { left: 0; right: 0; text-align: center; bottom: 14px; color: #fde7d2; }
</style>
</head>
<body>

<svg class="board-shapes" width="900" height="1200" viewBox="0 0 900 1200">
  <path d="M680 0 H900 V60 C860 100 820 140 760 130 C700 120 690 60 680 0 Z" fill="var(--board-blush)"/>
  <path d="M0 930 C40 880 110 870 150 900 C190 935 160 990 200 1040 C250 1100 400 1140 420 1200 H0 Z" fill="var(--board-blush)"/>
  <path d="M515 140 C520 80 570 20 650 0 H700 C700 60 640 120 560 140 Z" fill="var(--board-sage)" role="img" aria-label="Large sage leaf illustration"/>
  <path d="M60 1030 C90 1010 140 1050 170 1090 C210 1140 230 1180 220 1200 H60 C40 1150 30 1060 60 1030 Z" fill="var(--board-rose)" role="img" aria-label="Faint pink leaf illustration"/>
</svg>

<p class="board-label">10x10in High Resolution JPG<br>Social Posts</p>

<!-- Post 1 -->
<article class="post post-grow">
  <svg class="art" width="392" height="392" viewBox="0 0 392 392">
    <defs>
      <linearGradient id="grow-leaves" x1="0" y1="0" x2="1" y2="1">
        <stop offset="0" stop-color="#1fb8a8"/>
        <stop offset="1" stop-color="#c9f0eb"/>
      </linearGradient>
      <linearGradient id="grow-corner-right" x1="1" y1="0" x2="0" y2="1">
        <stop offset="0" stop-color="#1fb8a8"/>
        <stop offset="0.5" stop-color="#ffd84a"/>
        <stop offset="1" stop-color="#d3f3ef"/>
      </linearGradient>
      <linearGradient id="grow-figure" x1="0" y1="0" x2="1" y2="1">
        <stop offset="0" stop-color="#8a3aa0"/>
        <stop offset="0.35" stop-color="#14bfae"/>
        <stop offset="1" stop-color="#f5ae2c"/>
      </linearGradient>
    </defs>
    <path d="M160 80 C200 55 280 60 320 100 C360 140 350 230 320 262 C290 290 220 285 180 262 C140 240 135 180 140 140 C145 110 145 92 160 80 Z" fill="var(--soft-pink)"/>
    <path d="M0 0 H100 C110 30 85 60 95 95 C100 130 70 150 55 130 C40 115 20 140 0 128 Z" fill="url(#grow-leaves)" opacity="0.75" role="img" aria-label="Teal tropical leaves in the corner"/>
    <path d="M392 0 V170 C370 175 345 160 340 130 C332 100 345 80 335 55 C328 30 345 10 360 0 Z" fill="url(#grow-corner-right)" opacity="0.8" role="img" aria-label="Teal leaves and yellow flower in the corner"/>
    <path d="M95 140 C120 130 135 150 125 175 C115 200 110 215 120 240 C135 270 150 275 140 295 C130 320 110 335 80 335 C45 335 18 310 15 280 C12 250 30 230 40 205 C50 175 65 150 95 140 Z" fill="url(#grow-figure)" role="img" aria-label="Illustration of a woman on a ladder reaching a purple flower among leaves"/>
  </svg>
  <div class="quote">
    <p class="line" style="top:38px;font-size:46px;">“Don’t</p>
    <p class="line accent-pink" style="top:84px;font-size:68px;">Go</p>
    <p class="line" style="top:148px;font-size:56px;">Through Life,</p>
    <p class="line accent-teal" style="top:198px;font-size:66px;">Grow</p>
    <p class="line" style="top:264px;font-size:56px;">Through Life”</p>
  </div>
  <p class="author">– Milo Pendrake</p>
  <p class="handle">@QuillmoreStudio</p>
</article>

<!-- Post 2 -->
<article class="post post-balance">
  <svg class="art" width="392" height="392" viewBox="0 0 392 392">
    <defs>
      <linearGradient id="balance-rider" x1="0" y1="0" x2="0.6" y2="1">
        <stop offset="0" stop-color="#f2c2a8"/>
        <stop offset="0.45" stop-color="#fbfbfb"/>
        <stop offset="1" stop-color="#f07aa0"/>
      </linearGradient>
      <linearGradient id="balance-teal" x1="0" y1="0" x2="1" y2="1">
        <stop offset="0" stop-color="#13c3b4"/>
        <stop offset="1" stop-color="#0e6b6c"/>
      </linearGradient>
    </defs>
    <circle cx="233" cy="161" r="115" fill="var(--coral)"/>
    <path d="M0 0 H55 C65 20 50 35 30 40 C20 55 22 70 14 66 C5 60 4 45 0 40 Z" fill="#f98a5a" role="img" aria-label="Orange and teal leaves in the corner"/>
    <path d="M392 28 V122 C375 125 360 115 345 108 C338 95 360 85 352 70 C345 55 335 45 345 35 C360 25 380 30 392 28 Z" fill="url(#balance-teal)" role="img" aria-label="Teal leaves on the right edge"/>
    <path d="M0 154 C25 150 45 170 38 190 C30 205 45 220 30 230 C15 240 40 260 35 280 C30 300 15 312 0 315 Z" fill="url(#balance-teal)" role="img" aria-label="Teal leaves on the left edge"/>
    <path d="M95 166 C115 160 130 175 128 195 C126 215 130 240 138 265 C145 290 140 320 130 345 C118 372 95 380 75 370 C55 360 45 335 52 310 C60 285 75 265 80 240 C85 215 78 175 95 166 Z" fill="url(#balance-rider)" role="img" aria-label="Illustration of a woman in a white dress riding a pink bicycle"/>
  </svg>
  <div class="quote">
    <p class="line" style="top:50px;">“Life is like</p>
    <p class="line" style="top:86px;">riding a bicycle.</p>
    <p class="line" style="top:124px;">To keep your</p>
    <p class="line accent-yellow" style="top:161px;">BALANCE,</p>
    <p class="line" style="top:197px;">you must keep</p>
    <p class="line accent-yellow" style="top:231px;">MOVING.”</p>
  </div>
  <p class="author">—Lucian Thornwick</p>
  <p class="handle">@QuillmoreStudio</p>
</article>

<!-- Post 3 -->
<article class="post post-bliss">
  <svg class="art" width="405" height="405" viewBox="0 0 405 405">
    <defs>
      <linearGradient id="bliss-arch" x1="0" y1="0" x2="0.7" y2="1">
        <stop offset="0" stop-color="#2b1d6b"/>
        <stop offset="0.6" stop-color="#3a2a7e"/>
        <stop offset="1" stop-color="#1597a4"/>
      </linearGradient>
    </defs>
    <path d="M151 350 V252 A51 51 0 0 1 253 252 V340 A10 10 0 0 1 243 350 H161 A10 10 0 0 1 151 340 Z" fill="url(#bliss-arch)" role="img" aria-label="Illustration of a woman climbing teal stairs under a starry night arch"/>
  </svg>
  <div class="quote">
    <p class="line ink-navy" style="top:26px;">Follow Your Bliss</p>
    <p class="line ink-white" style="top:56px;">And The Universe</p>
    <p class="line ink-navy" style="top:87px;">Will <span class="big">Open Doors</span></p>
    <p class="line ink-white" style="top:119px;">Where There Were</p>
    <p class="line ink-white" style="top:150px;">Only Walls</p>
  </div>
  <p class="author">– Arthur Venholm</p>
  <p class="handle">@QuillmoreStudio</p>
</article>

</body>
</html>
```